Lawn & Garden Maintenace Business card design needed

I need a basic business card design for a Lawn Mowing & Garden Maintenance business

I would like it to look a combination of classy, striking, with vibrant Green/s, I will attached a very rough idea of what I would like but I am open to new suggestions, and the possibility of doing it on a darker charcoal or black gloss card, please don't just send me a version of what I've attached it's a very rough idea & more based around the text layout than anything else, feel free to let your creative instincts fly!

Must have grass across the bottom of the Card & i would prefer it to be portrait rather than landscape.

I quite like the coloring of this previously submitted card
http://www.artspark-example.com/design/2840613

Please have the text in White and Green if you are submitting a dark card, thank you.

Business

R.K. Lawn & Garden Services

Free Quote - Great Rates

Rob Kessler
0417 362 918
Info@RKLawnAndGarden.example.au

Requirements
Must have
• Must have grass across bottom of card preferably photo real grass rather than illustrated.
Nice to have
• Small telephone icon for phone number small email icon for email address but only if both icon are similar size and don't take away from the overall look of the card

Would also be nice to a have a flow/style that would be easily transferable to flyers & advertising

```html
<!DOCTYPE html>
<html lang="en">
<head>
<meta charset="utf-8">
<title>R.K. Lawn &amp; Garden Services – Business Card</title>
<link rel="stylesheet" href="https://fonts.googleapis.com/css2?family=EB+Garamond:wght@500&family=Noto+Serif:wght@400&display=swap">
<style>
  :root {
    --paper: #ffffff;
    --leaf: #2aa61a;
    --leaf-light: #8fd66a;
    --leaf-pale: #d9f2c9;
    --grass-dark: #2f8a12;
    --grass-mid: #52c21f;
    --grass-light: #b7eb8a;
    --ink: #151515;
    --shadow: rgba(0,0,0,0.28);
  }
  * { margin: 0; padding: 0; box-sizing: border-box; }
  html, body { width: 783px; height: 1200px; overflow: hidden; background: var(--paper); }
  .card {
    position: relative;
    width: 783px; height: 1200px;
    background: var(--paper);
    overflow: hidden;
    font-family: "EB Garamond", Georgia, serif;
    color: var(--ink);
  }
  .corner-vine {
    position: absolute; top: 0;
    width: 175px; height: 385px;
  }
  .corner-vine--left {
    left: 0;
    background: radial-gradient(ellipse at 25% 25%, var(--leaf-light) 0%, var(--leaf-pale) 55%, rgba(255,255,255,0) 78%);
  }
  .corner-vine--right {
    right: 0;
    background: radial-gradient(ellipse at 75% 25%, var(--leaf-light) 0%, var(--leaf-pale) 55%, rgba(255,255,255,0) 78%);
  }
  .brand {
    position: absolute; left: 0; right: 0; top: 70px;
    text-align: center;
    color: var(--leaf);
    font-weight: 500;
    line-height: 1;
  }
  .brand__initials { display: block; font-size: 150px; letter-spacing: 6px; height: 190px; }
  .brand__lawn { display: block; font-size: 104px; letter-spacing: 2px; margin-top: 4px; }
  .brand__garden { display: block; font-size: 60px; margin-top: -2px; }
  .brand__services { display: block; font-size: 72px; margin-top: 0; }
  .services-list {
    position: absolute; left: 0; right: 0; top: 518px;
    text-align: center; font-size: 24px; color: var(--ink);
  }
  .tagline {
    position: absolute; left: 0; right: 0; top: 553px;
    text-align: center; font-size: 40px; color: var(--leaf);
    letter-spacing: 1px;
  }
  .contact {
    position: absolute; left: 0; right: 0; top: 688px;
    text-align: center;
    font-family: "Noto Serif", Georgia, serif;
    text-shadow: 2px 2px 2px var(--shadow);
  }
  .contact__name { font-size: 44px; line-height: 56px; }
  .contact__line {
    display: flex; justify-content: center; align-items: center; gap: 4px;
    font-size: 31px; line-height: 46px;
  }
  .contact__icon { width: 36px; height: 28px; flex: none; }
  .grass {
    position: absolute; left: 0; right: 0; bottom: 0; height: 330px;
    background: linear-gradient(to bottom, rgba(255,255,255,0) 0%, var(--grass-light) 14%, var(--grass-mid) 42%, var(--grass-dark) 100%);
  }
</style>
</head>
<body>
<main class="card">
  <div class="corner-vine corner-vine--left" role="img" aria-label="Green rose and vine ornament in the top left corner"></div>
  <div class="corner-vine corner-vine--right" role="img" aria-label="Green rose and vine ornament in the top right corner"></div>

  <h1 class="brand" aria-label="R.K. Lawn &amp; Garden Services">
    <span class="brand__initials">R.K.</span>
    <span class="brand__lawn">LAWN</span>
    <span class="brand__garden">&amp; GARDEN</span>
    <span class="brand__services">SERVICES</span>
  </h1>

  <p class="services-list">Mowing Edging Trimming Wedding Planting &amp; More</p>
  <p class="tagline">FREE QUOTE - GREAT RATES</p>

  <section class="contact">
    <p class="contact__name">Rob Kessler</p>
    <p class="contact__line">
      <svg class="contact__icon" viewBox="0 0 36 28" aria-hidden="true">
        <path d="M3 10 Q18 -2 33 10 L30 14 L25 12 L24 8 Q18 6 12 8 L11 12 L6 14 Z" fill="#151515"/>
        <path d="M9 14 L27 14 L31 25 L5 25 Z" fill="#151515"/>
        <circle cx="18" cy="19.5" r="3.2" fill="#fff"/>
      </svg>
      <span>: 0417 362 918</span>
    </p>
    <p class="contact__line">
      <svg class="contact__icon" viewBox="0 0 36 28" aria-hidden="true">
        <rect x="2" y="3" width="32" height="22" fill="#fff" stroke="#151515" stroke-width="2"/>
        <path d="M2 3 L18 16 L34 3" fill="none" stroke="#151515" stroke-width="2"/>
        <circle cx="18" cy="14" r="5" fill="#fff" stroke="#151515" stroke-width="1.6"/>
        <text x="18" y="17.5" font-size="9" text-anchor="middle" font-family="Noto Serif, serif" fill="#151515">@</text>
      </svg>
      <span>: Rob@rklawnandgarden.example.au</span>
    </p>
  </section>

  <div class="grass" role="img" aria-label="Photo of lush green grass blades across the bottom of the card"></div>
</main>
</body>
</html>
```